Harborlight Behavioral and Community Services

Intellectual Developmental Disabilities, Group Homes, Residential Homes and Substance Abuse Residential facilities

Target Market(s)

Adults 18-59 male and female autism, developmental disabilities and mental health

Industry/Entity Type

Intellectual Development Disabilities, Autism, Applied Behavioral Analysis, Mental Health, Substance Abuse

Coding

Coded - Design and coding required

Number of Pages Required

5+ page

Font styles to use
Serif

Colors
0054AA
0677BA
7BADD7
CADEEF
E8F1F8

Requirements
Should not have
• Not specified

```html
<!DOCTYPE html>
<html lang="en">
<head>
<meta charset="utf-8">
<title>Harborlight Behavioral and Community Services</title>
<link rel="stylesheet" href="https://fonts.googleapis.com/css2?family=Arimo:wght@400;700&display=swap">
<style>
:root{
  --navy:#0a3d98;
  --blue:#0677BA;
  --bright:#1592e0;
  --why:#1189df;
  --sky:#7BADD7;
  --pale:#CADEEF;
  --mist:#E3EFF9;
  --ink:#2b2b2b;
  --text:#3a3a3a;
  --white:#fff;
}
*{margin:0;padding:0;box-sizing:border-box}
html,body{width:1200px;height:4751px;overflow:hidden}
body{position:relative;background:var(--white);font-family:"Arimo",Arial,sans-serif;color:var(--text)}
.abs{position:absolute}
.btn{position:absolute;display:flex;align-items:center;justify-content:center;border-radius:24px;background:var(--bright);color:#fff;font-weight:700;font-size:16px}
.photo{position:absolute;overflow:hidden}

/* top bar */
.topbar{left:0;top:0;width:1200px;height:48px;background:linear-gradient(90deg,#1a9be6,#0a4aa8)}
.topbar .help{left:0;width:1200px;top:15px;text-align:center;color:#fff;font-weight:700;font-size:15px}
.topbar .login{left:1000px;top:15px;color:#fff;font-weight:700;font-size:15px}

/* header */
.brand{display:flex;align-items:center;gap:10px}
.brand .dot{width:46px;height:46px;border-radius:50%;background:var(--navy)}
.brand .name{color:var(--navy);font-weight:700;font-size:30px;line-height:1}
.brand .name small{display:block;font-size:12px;margin-top:3px}
.nav{top:83px;font-size:16px;color:#222}
.nav span{position:absolute;white-space:nowrap}

/* hero */
.hero{left:0;top:151px;width:1200px;height:501px;background:var(--mist)}
.clip{left:0;top:151px;width:1200px;height:501px;overflow:hidden}
.outline-diamond{left:1020px;top:-40px;width:200px;height:200px;border:2px solid var(--bright);border-radius:36px;transform:rotate(45deg)}
.tri{left:340px;top:431px;width:171px;height:171px;background:#a8d1ee;border-radius:26px;transform:rotate(45deg)}
.diamond{overflow:hidden;border-radius:90px;transform:rotate(45deg)}
.hero h1{left:125px;top:247px;font-size:48px;font-weight:400;line-height:56px;color:var(--ink)}
.hero-lead{left:125px;top:369px;width:440px;font-size:20px;line-height:29px;color:#333}

/* headings */
.h2{font-size:46px;font-weight:400;color:var(--ink);line-height:1.1}
.center{left:0;width:1200px;text-align:center}
.para{font-size:16.5px;line-height:26px;color:#444}

/* services */
.svc-bg{left:0;top:1419px;width:1200px;height:700px}
.svc{top:1581px;width:184px;height:196px;border-radius:30px;background:#fff;box-shadow:0 6px 18px rgba(10,60,140,.08);display:flex;flex-direction:column;align-items:center;justify-content:flex-end;padding-bottom:30px;text-align:center;font-weight:700;font-size:17px;line-height:21px;color:#222}
.svc svg{margin-bottom:14px}
.svc.active{background:linear-gradient(180deg,#0a47b8,#1aa2ee);color:#fff}
.detail{left:111px;top:1843px;width:978px;height:433px;background:#fff;border-radius:36px;box-shadow:0 8px 30px rgba(10,60,140,.1)}
.detail h3{left:55px;top:83px;font-size:33px;line-height:40px;color:#111;font-weight:700}
.detail p{left:55px;top:180px;width:440px;font-size:16.5px;line-height:21px;color:#333}

/* facilities */
.fac{width:214px;height:214px;border-radius:50%;top:2560px}
.fac-label{top:2803px;width:300px;text-align:center;font-size:21px;line-height:26px;color:#444}

/* why */
.why{left:0;top:2962px;width:1200px;height:554px;background:var(--why);border-radius:0 100px 0 40px}
.why h2{left:111px;top:3112px;font-size:40px;line-height:48px;font-weight:400;color:#fff}
.why p{left:111px;top:3237px;width:430px;font-size:20px;line-height:28px;color:#fff}

/* news */
.news-img{top:3690px;width:305px;height:236px;border-radius:0 40px 0 0}
.news-title{top:3960px;width:305px;font-size:22px;line-height:26px;font-weight:700;color:#222}
.news-text{top:4040px;width:290px;font-size:16px;line-height:25px;color:#444}
.news-more{top:4140px;font-size:16px;font-weight:700;color:var(--bright)}

/* footer */
.foot-text{color:#fff}
.foot-h{font-size:24px;color:#fff}
.foot-rule{height:2px;background:var(--bright)}
.foot-links span{position:absolute;font-size:14px;color:#fff;white-space:nowrap}
.social{width:33px;height:33px;border-radius:50%;border:2px solid #fff}
.cicon{width:37px;height:37px;border-radius:50%;background:var(--bright);display:flex;align-items:center;justify-content:center}
</style>
</head>
<body>

<!-- top bar -->
<div class="abs topbar">
  <div class="abs help">We can help: (000) 555-0142</div>
  <div class="abs login">Patient Login</div>
</div>

<!-- header -->
<div class="abs brand" style="left:88px;top:72px">
  <span class="dot"></span>
  <span class="name">Harborlight<small>Behavioral &amp; Community Services</small></span>
</div>
<nav class="abs nav" style="left:0">
  <span style="left:446px">Home</span>
  <span style="left:527px">Our Services</span>
  <span style="left:662px">About Us</span>
  <span style="left:774px">Foundation</span>
  <span style="left:900px">Contact</span>
</nav>
<div class="btn" style="left:993px;top:70px;width:109px;height:46px">Donate</div>

<!-- hero -->
<section class="abs hero"></section>
<div class="abs clip">
  <div class="abs outline-diamond"></div>
  <div class="abs tri"></div>
</div>
<h1 class="abs" style="left:125px;top:247px;font-size:48px;font-weight:400;line-height:56px;color:var(--ink)">Welcome to Harborlight<br>Community Programs</h1>
<p class="abs hero-lead">Intellectual Developmental Disabilities, Group Homes, Residential Homes and Substance Abuse Residential facilities</p>
<div class="btn" style="left:125px;top:475px;width:144px;height:46px">Donate Now</div>
<div class="abs diamond" style="left:634px;top:262px;width:391px;height:391px;background:linear-gradient(135deg,#b07a48,#d8a277 50%,#7a5a3c)" role="img" aria-label="Photo of two smiling friends embracing cheek to cheek"></div>

<!-- about -->
<div class="photo" style="left:109px;top:816px;width:413px;height:474px;border-radius:0 90px 0 90px;background:linear-gradient(140deg,#8a7a6a,#c9a58a 50%,#5a6a7a)" role="img" aria-label="Photo of women sharing a warm group hug"></div>
<h2 class="abs h2" style="left:582px;top:852px;font-size:44px;line-height:46px">About Harborlight<br>Community Programs</h2>
<p class="abs para" style="left:582px;top:963px;width:480px">Lorem ipsum dolor sit amet, consectetur adipiscing elised do eiusmod tempor incididunt ut labore et dolore magna aliqua. Quis ipsum suspendisse ultrices gravida. Risus commodo viverra maecenas accumsan lacus vel facilisis. Lorem ipsum dolor sit amet, consectetur adipiscing elit, sed do eiusmod tempor incididunt ut labore et dolore magna aliquauis ipsum suspendisse ultrices gravida. Risus commodo viverra maecenas accumsan lacus vel facilisis.</p>
<div class="btn" style="left:582px;top:1196px;width:150px;height:55px;border-radius:28px">Read More</div>

<!-- services -->
<svg class="abs svc-bg" width="1200" height="700" viewBox="0 0 1200 700" aria-hidden="true">
  <rect width="1200" height="700" fill="#E3EFF9"/>
  <path d="M0 627 Q600 420 1200 666 V700 H0Z" fill="#fff"/>
</svg>
<h2 class="abs h2 center" style="top:1484px">Our Services</h2>

<div class="abs svc active" style="left:109px">
  <svg width="64" height="80" viewBox="0 0 64 80" fill="none" stroke="#fff" stroke-width="2.5"><path d="M14 74V56C6 50 4 40 6 30 9 14 22 6 36 8c14 2 22 14 20 28l6 12h-6v10c0 4-3 6-7 6h-7v10"/><circle cx="32" cy="30" r="12"/></svg>
  Intellectual<br>Development<br>Disabilities
</div>
<div class="abs svc" style="left:308px">
  <svg width="72" height="80" viewBox="0 0 72 80" fill="none" stroke="#0a55b8" stroke-width="2.5"><path d="M14 74V56C6 50 4 40 6 30 9 14 22 6 36 8c14 2 22 14 20 28l6 12h-6v10c0 4-3 6-7 6h-7v10"/><rect x="24" y="20" width="14" height="14"/><rect x="38" y="20" width="14" height="14"/><rect x="24" y="34" width="14" height="14"/></svg>
  Autism
</div>
<div class="abs svc" style="left:507px">
  <svg width="72" height="80" viewBox="0 0 72 80" fill="none" stroke="#0a55b8" stroke-width="2.5"><path d="M14 74V56C6 50 4 40 6 30 9 14 22 6 36 8c14 2 22 14 20 28l6 12h-6v10c0 4-3 6-7 6h-7v10"/><circle cx="30" cy="30" r="9"/><circle cx="30" cy="30" r="3"/><path d="M44 24l12 6-12 6"/></svg>
  Applied<br>Behavioral<br>Analysis
</div>
<div class="abs svc" style="left:706px">
  <svg width="72" height="80" viewBox="0 0 72 80" fill="none" stroke="#0a55b8" stroke-width="2.5"><path d="M14 74V56C6 50 4 40 6 30 9 14 22 6 36 8c14 2 22 14 20 28l6 12h-6v10c0 4-3 6-7 6h-7v10"/><path d="M32 40c-8-6-12-10-12-15a6 6 0 0 1 12-2 6 6 0 0 1 12 2c0 5-4 9-12 15z"/></svg>
  Mental<br>Health
</div>
<div class="abs svc" style="left:904px">
  <svg width="80" height="80" viewBox="0 0 80 80" fill="none" stroke="#0a55b8" stroke-width="2.5"><circle cx="40" cy="40" r="36"/><circle cx="40" cy="40" r="28"/><path d="M30 56V34a3 3 0 0 1 6 0v-8a3 3 0 0 1 6 0v6a3 3 0 0 1 6 0v16c0 6-4 10-10 10h-2c-3 0-6-2-6-4z"/></svg>
  Substance<br>Abuse
</div>

<div class="abs detail">
  <h3 class="abs">Intellectual<br>Development Disabilities</h3>
  <p class="abs">Lorem ipsum dolor sit amet, consectetur adipiscing elit, sed do eiusmod tempor incididunt ut labore et dolore magna aliqua. Quis ipsum suspendisse ultrices gravida. Risus commodo viverra maecenas accumsan lacus vel facilisis.</p>
  <div class="btn" style="left:55px;top:299px;width:151px;height:52px;border-radius:26px">Read More</div>
  <div class="photo" style="left:540px;top:42px;width:395px;height:345px;border-radius:40px;background:linear-gradient(135deg,#c98a4a,#e8d7c2 55%,#7a8a9a)" role="img" aria-label="Photo of a caregiver assisting a smiling woman in a wheelchair"></div>
</div>

<!-- facilities -->
<h2 class="abs h2 center" style="top:2369px">Our Facilities</h2>
<p class="abs para" style="left:249px;top:2451px;width:702px;text-align:center">Lorem ipsum dolor sit amet, consectetur adipiscing elised do eiusmod tempor incididunt ut labore et dolore magna aliqua. Quis ipsum suspendisse ultrices gravida. Risus commodo viverra maecenas accumsan lacus vel facilisisorem ipsum dolor sit amet.</p>
<div class="photo fac" style="left:184px;background:linear-gradient(135deg,#b8a898,#6a7e98)" role="img" aria-label="Photo of a support group session in a group home"></div>
<div class="photo fac" style="left:490px;background:linear-gradient(135deg,#e8e2dc,#c9a59a)" role="img" aria-label="Photo of a smiling resident at home"></div>
<div class="photo fac" style="left:798px;background:linear-gradient(135deg,#8a8a8a,#5a6a7a 60%,#c7934a)" role="img" aria-label="Photo of a counseling circle at a residential facility"></div>
<div class="abs fac-label" style="left:141px;top:2802px">Group Homes</div>
<div class="abs fac-label" style="left:447px;top:2802px">Residential Homes</div>
<div class="abs fac-label" style="left:755px;top:2790px">Substance Abuse<br>Residential facilities</div>

<!-- why choose -->
<section class="abs why"></section>
<h2 class="abs" style="left:111px;top:3112px;font-size:40px;line-height:48px;font-weight:400;color:#fff">Why Choose Harborlight<br>Community Programs</h2>
<p class="abs" style="left:111px;top:3237px;width:430px;font-size:20px;line-height:28px;color:#fff">Intellectual Developmental Disabilities, Group Homes, Residential Homes and Substance Abuse Residential facilities</p>
<div class="btn" style="left:111px;top:3341px;width:141px;height:47px;background:var(--navy)">Read More</div>
<div class="abs diamond" style="left:634px;top:3044px;width:391px;height:391px;background:linear-gradient(135deg,#9ab0a0,#d8cbb8 50%,#8aa27a)" role="img" aria-label="Photo of two women laughing together at a table"></div>

<!-- news -->
<h2 class="abs h2 center" style="top:3598px">Latest News</h2>

<div class="photo news-img" style="left:107px;background:linear-gradient(135deg,#8a9a6a,#d8a830 60%,#c9b89a)" role="img" aria-label="Photo of a young man reading his phone"></div>
<div class="photo news-img" style="left:446px;background:linear-gradient(135deg,#d8dde2,#8a8a8a)" role="img" aria-label="Photo of a stressed woman at a laptop"></div>
<div class="photo news-img" style="left:785px;background:linear-gradient(135deg,#c8d0d8,#7a8aa0)" role="img" aria-label="Photo of a man laughing in a group session"></div>

<div class="abs news-title" style="left:107px">Lorem ipsum dolor sit ame consectetur adipiscing.</div>
<div class="abs news-title" style="left:446px">Lorem ipsum dolor sit ame consectetur adipiscing.</div>
<div class="abs news-title" style="left:785px">Lorem ipsum dolor sit ame consectetur adipiscing.</div>
<p class="abs news-text" style="left:107px">smod tempor incididunt ut labore et dolore magna aliqua. Quis ipsum suspendisse ultrices gravida</p>
<p class="abs news-text" style="left:446px">smod tempor incididunt ut labore et dolore magna aliqua. Quis ipsum suspendisse ultrices gravida</p>
<p class="abs news-text" style="left:785px">smod tempor incididunt ut labore et dolore magna aliqua. Quis ipsum suspendisse ultrices gravida</p>
<div class="abs news-more" style="left:107px">Read More</div>
<div class="abs news-more" style="left:446px">Read More</div>
<div class="abs news-more" style="left:785px">Read More</div>

<!-- footer -->
<svg class="abs" style="left:0;top:4270px" width="1200" height="481" viewBox="0 0 1200 481" aria-hidden="true">
  <path d="M0 100 Q600 -60 1200 100 V481 H0Z" fill="#1a9be6"/>
  <path d="M0 118 Q600 -30 1200 118 V481 H0Z" fill="#fff"/>
  <path d="M0 128 Q600 -10 1200 128 V481 H0Z" fill="#0a3d98"/>
</svg>

<div class="abs brand" style="left:111px;top:4458px">
  <span class="dot" style="background:#fff;width:52px;height:52px"></span>
  <span class="name" style="color:#fff">Harborlight<small>Behavioral &amp; Community Services</small></span>
</div>
<p class="abs foot-text" style="left:107px;top:4531px;width:350px;font-size:14px;line-height:18px">Lorem ipsum dolor sit amet, consectetur adipiscing elit, sed do eiusmod tempor incididunt ut labore et dolore magna aliqua. Quis ipsum suspendisse.</p>
<span class="abs social" style="left:108px;top:4613px"></span>
<span class="abs social" style="left:148px;top:4613px"></span>
<span class="abs social" style="left:188px;top:4613px"></span>
<span class="abs social" style="left:227px;top:4613px"></span>

<div class="abs foot-h" style="left:577px;top:4412px">Links</div>
<div class="abs foot-rule" style="left:577px;top:4454px;width:129px"></div>
<div class="abs foot-links" style="left:579px;top:0">
  <span style="top:4484px">Home</span>
  <span style="top:4510px">Who We Are</span>
  <span style="top:4537px">Services</span>
  <span style="top:4563px">Blog</span>
  <span style="top:4589px">Contact Us</span>
</div>

<div class="abs foot-h" style="left:846px;top:4412px">Contact</div>
<div class="abs foot-rule" style="left:846px;top:4454px;width:129px"></div>
<div class="abs cicon" style="left:843px;top:4490px">
  <svg width="16" height="16" viewBox="0 0 24 24" fill="#fff"><path d="M6.6 10.8a15 15 0 0 0 6.6 6.6l2.2-2.2c.3-.3.7-.4 1-.2 1.1.4 2.3.6 3.6.6.6 0 1 .4 1 1V20c0 .6-.4 1-1 1A17 17 0 0 1 3 4c0-.6.4-1 1-1h3.5c.6 0 1 .4 1 1 0 1.3.2 2.5.6 3.6.1.3 0 .7-.2 1z"/></svg>
</div>
<div class="abs foot-text" style="left:896px;top:4491px;font-size:14px;line-height:18px">Phone:<br>555 204 7183</div>
<div class="abs cicon" style="left:843px;top:4558px">
  <svg width="16" height="16" viewBox="0 0 24 24" fill="#fff"><path d="M3 5h18v14H3z" fill="none" stroke="#fff" stroke-width="2"/><path d="M3 6l9 7 9-7" fill="none" stroke="#fff" stroke-width="2"/></svg>
</div>
<div class="abs foot-text" style="left:896px;top:4559px;font-size:14px;line-height:18px">Email:<br>hello@harborlight.org</div>

<div class="abs foot-text center" style="top:4682px;font-size:14px">Copyright © 2025 All Rights are reserved.</div>

</body>
</html>
```